Dental Office Business Card

We need a business card for our pediatric dentistry office.
On one side the design needs to contain the following:
our logo (attached)
Vento Pediatric Grins
Soraya Kadbelani, DDS
Board Certified Pediatric Dentist
Tel: (555) 318-2747)
Fax: (555) 264-8031
Email: info@ventopediatricgrins.example
Web: www.ventopediatricgrins.example
Address: 41 Brindle Ave, Suite 208, Wellesley, MA 02099

On the other side of the card, the design needs to have an appointment reminder (date and time as well as day of the week) similar to the design attached (no need for appointment reason “For”)

```html
<!DOCTYPE html>
<html lang="en">
<head>
<meta charset="UTF-8">
<title>Vento Pediatric Grins — Business Card</title>
<link rel="stylesheet" href="https://fonts.googleapis.com/css2?family=Montserrat:wght@500;600;700;800&family=Open+Sans:wght@400;600&display=swap">
<style>
  :root {
    --ink: #231f20;
    --mint: #9fdcac;
    --mint-soft: #e9f6ec;
    --paper: #ffffff;
    --stage: #2a2a2a;
  }
  * { box-sizing: border-box; margin: 0; padding: 0; }
  html, body { width: 1200px; height: 780px; overflow: hidden; }
  body {
    background: var(--stage);
    display: flex; align-items: center; justify-content: center; gap: 40px;
    font-family: "Open Sans", Arial, sans-serif;
    color: var(--ink);
  }
  .card {
    position: relative;
    width: 540px; height: 310px;
    background: var(--paper);
    border-radius: 22px;
    border: 3px solid var(--mint);
    overflow: hidden;
  }

  /* brand lockup */
  .brand { display: flex; align-items: center; gap: 12px; }
  .brand-dot { width: 40px; height: 40px; border-radius: 50%; background: var(--mint); flex: none; }
  .brand-text { font-family: "Montserrat", Arial, sans-serif; font-weight: 700; color: var(--ink); line-height: 1; }
  .brand-name { font-size: 44px; letter-spacing: -0.5px; }
  .brand-sub { font-size: 16px; letter-spacing: 0.6px; margin-top: 4px; }

  /* appointment side */
  .appointment .brand { position: absolute; top: 34px; left: 50%; transform: translateX(-50%); }
  .appointment .brand-name { font-size: 38px; }
  .appointment .brand-sub { font-size: 14px; }
  .appt-title {
    position: absolute; top: 128px; width: 100%; text-align: center;
    font-family: "Montserrat", Arial, sans-serif; font-weight: 600; font-size: 14px;
  }
  .days {
    position: absolute; top: 162px; left: 30px; right: 30px;
    display: flex; justify-content: space-between;
    font-family: "Montserrat", Arial, sans-serif; font-weight: 500; font-size: 13px;
  }
  .day { display: flex; align-items: center; gap: 5px; }
  .box { width: 15px; height: 15px; border: 2px solid var(--ink); }
  .fill-in {
    position: absolute; top: 204px; left: 60px; right: 60px;
    display: flex; align-items: flex-end; gap: 8px;
    font-family: "Montserrat", Arial, sans-serif; font-weight: 500; font-size: 13px;
  }
  .blank { flex: 1; border-bottom: 2px solid var(--ink); height: 14px; }
  .blank.short { flex: 0 0 110px; }
  .notice-band {
    position: absolute; left: 0; right: 0; bottom: 0; height: 40px;
    background: var(--ink); color: var(--paper);
    display: flex; align-items: center; justify-content: center;
    font-size: 10.5px; letter-spacing: 0.3px; text-transform: uppercase;
  }

  /* contact side */
  .contact .brand { position: absolute; top: 108px; left: 28px; gap: 10px; }
  .contact .brand-name { font-size: 40px; }
  .contact .brand-sub { font-size: 14.5px; }
  .divider { position: absolute; left: 290px; top: 52px; height: 178px; width: 1px; background: var(--ink); }
  .details { position: absolute; left: 310px; top: 44px; right: 16px; }
  .person { font-family: "Montserrat", Arial, sans-serif; font-weight: 700; font-size: 15px; }
  .role { font-family: "Montserrat", Arial, sans-serif; font-weight: 700; font-size: 7.5px; letter-spacing: 0.3px; margin-top: 2px; text-transform: uppercase; }
  .address { font-size: 10.5px; line-height: 1.3; margin-top: 18px; }
  .lines { list-style: none; margin-top: 10px; }
  .lines li { display: flex; align-items: center; gap: 7px; font-size: 10.5px; line-height: 1; margin-bottom: 5px; }
  .icon { width: 13px; height: 13px; border-radius: 50%; background: var(--mint); display: flex; align-items: center; justify-content: center; flex: none; }
  .icon svg { width: 8px; height: 8px; }
  .ink-band { position: absolute; left: 0; width: 400px; bottom: 26px; height: 16px; background: var(--ink); }
  .mint-band { position: absolute; right: 0; width: 90px; bottom: 42px; height: 14px; background: var(--mint); }
  .corner-dot { position: absolute; right: 96px; bottom: 36px; width: 26px; height: 26px; border-radius: 50%; background: var(--mint); }
</style>
</head>
<body>

<section class="card appointment" aria-label="Appointment reminder side">
  <div class="brand">
    <span class="brand-dot"></span>
    <div class="brand-text">
      <div class="brand-name">Vento</div>
      <div class="brand-sub">PEDIATRIC GRINS</div>
    </div>
  </div>
  <p class="appt-title">Your next appointment</p>
  <div class="days">
    <span class="day"><span class="box"></span>Mon</span>
    <span class="day"><span class="box"></span>Tue</span>
    <span class="day"><span class="box"></span>Wed</span>
    <span class="day"><span class="box"></span>Thu</span>
    <span class="day"><span class="box"></span>Fri</span>
    <span class="day"><span class="box"></span>Sat</span>
    <span class="day"><span class="box"></span>Sun</span>
  </div>
  <div class="fill-in">
    <span>Date</span><span class="blank"></span>
    <span>At</span><span class="blank short"></span>
    <span>AM/PM</span>
  </div>
  <div class="notice-band">If unable to keep this appointment 48 hours notice is required.</div>
</section>

<section class="card contact" aria-label="Contact side">
  <div class="brand">
    <span class="brand-dot"></span>
    <div class="brand-text">
      <div class="brand-name">Vento</div>
      <div class="brand-sub">PEDIATRIC GRINS</div>
    </div>
  </div>
  <div class="divider"></div>
  <div class="details">
    <p class="person">Soraya Kadbelani, DDS</p>
    <p class="role">Board Certified Pediatric Dentist</p>
    <p class="address">41 Brindle Ave, Suite 208,<br>Fernhollow, QX 02099</p>
    <ul class="lines">
      <li><span class="icon"><svg viewBox="0 0 10 10"><path d="M2 1l2 2-1 1.2c.6 1.2 1.6 2.2 2.8 2.8L7 6l2 2-1.3 1.3C4.5 9 1 5.5.7 2.3z" fill="#fff"/></svg></span>(555) 318-2747)</li>
      <li><span class="icon"><svg viewBox="0 0 10 10"><rect x="1.5" y="3.5" width="7" height="4.5" fill="#fff"/><rect x="3" y="1" width="4" height="3" fill="#fff"/></svg></span>(555) 264-8031</li>
      <li><span class="icon"><svg viewBox="0 0 10 10"><rect x="1" y="2.5" width="8" height="5.5" fill="#fff"/><path d="M1 2.5l4 3 4-3" stroke="#9fdcac" fill="none"/></svg></span>info@ventopediatricgrins.example</li>
      <li><span class="icon"><svg viewBox="0 0 10 10"><circle cx="5" cy="5" r="3.6" stroke="#fff" stroke-width="1.2" fill="none"/><path d="M1.4 5h7.2M5 1.4v7.2" stroke="#fff"/></svg></span>www.ventopediatricgrins.example</li>
    </ul>
  </div>
  <div class="mint-band"></div>
  <div class="corner-dot"></div>
  <div class="ink-band"></div>
</section>

</body>
</html>
```